Birchline Septic Solutions

Would like to see some single sided ones but would also like to see some double sided with one sided only being the logo. Owners name is Tom Halvick. Phone number is 555-214-0387
Services are pumping, inspections, installs, and repairs

Contact Information for Business Card

555-241-0387 Tom Halvick Elmbrook, OH

```html
<!DOCTYPE html>
<html lang="en">
<head>
<meta charset="UTF-8">
<title>Birchline Septic Solutions – Business Card</title>
<link href="https://fonts.googleapis.com/css2?family=Poppins:wght@700;800;900&display=swap" rel="stylesheet">
<style>
  :root {
    --backdrop: #f3f3f2;
    --card: #000000;
    --ink: #ffffff;
    --card-radius: 32px;
  }
  * { box-sizing: border-box; margin: 0; padding: 0; }
  html, body {
    width: 1200px;
    height: 1200px;
    overflow: hidden;
    background: var(--backdrop);
    font-family: "Poppins", Arial, sans-serif;
    color: var(--ink);
  }
  .canvas {
    position: relative;
    width: 1200px;
    height: 1200px;
  }
  .card {
    position: absolute;
    left: 410px;
    width: 681px;
    height: 396px;
    background: var(--card);
    border-radius: var(--card-radius);
    overflow: hidden;
  }
  .card-front { top: 197px; }
  .card-back { top: 672px; }

  /* Front */
  .brand {
    position: absolute;
    top: 168px;
    left: 0;
    width: 100%;
    text-align: center;
    font-weight: 800;
    color: var(--ink);
  }
  .brand-name {
    display: block;
    font-size: 66px;
    line-height: 1;
    letter-spacing: 2px;
  }
  .brand-tagline {
    display: block;
    margin-top: 10px;
    padding-left: 6px;
    font-size: 26px;
    line-height: 1;
    letter-spacing: 6px;
  }
  .location {
    position: absolute;
    top: 311px;
    left: 0;
    width: 100%;
    padding-left: 14px;
    text-align: center;
    font-weight: 700;
    font-size: 30px;
    line-height: 1;
    letter-spacing: 8px;
  }

  /* Back */
  .owner-name {
    position: absolute;
    top: 79px;
    right: 30px;
    font-weight: 800;
    font-size: 38px;
    letter-spacing: 6px;
    line-height: 1;
  }
  .contact {
    position: absolute;
    top: 170px;
    right: 32px;
    text-align: right;
  }
  .contact-callout {
    display: block;
    margin-right: 30px;
    font-weight: 800;
    font-size: 16px;
    letter-spacing: 3.5px;
    line-height: 1;
  }
  .contact-phone {
    display: block;
    margin-top: 7px;
    font-weight: 800;
    font-size: 42px;
    line-height: 1;
    letter-spacing: -0.5px;
  }
  .services {
    position: absolute;
    top: 204px;
    left: 40px;
  }
  .services-title {
    font-weight: 900;
    font-size: 28px;
    letter-spacing: 8px;
    line-height: 1;
    margin-bottom: 7px;
  }
  .services-list {
    list-style: none;
  }
  .services-list li {
    font-weight: 800;
    font-size: 18px;
    letter-spacing: 5px;
    line-height: 25.5px;
  }
  .services-list li::before {
    content: "•";
    display: inline-block;
    width: 26px;
    font-size: 12px;
    letter-spacing: 0;
    text-align: center;
    vertical-align: middle;
  }
</style>
</head>
<body>
  <main class="canvas">
    <section class="card card-front" aria-label="Business card front">
      <div class="brand">
        <span class="brand-name">BIRCHLINE</span>
        <span class="brand-tagline">SEPTIC SOLUTIONS</span>
      </div>
      <p class="location">ELMBROOK, OH</p>
    </section>

    <section class="card card-back" aria-label="Business card back">
      <h2 class="owner-name">TOM HALVICK</h2>
      <div class="contact">
        <span class="contact-callout">CALL US TODAY!</span>
        <span class="contact-phone">555-214-0387</span>
      </div>
      <div class="services">
        <h3 class="services-title">SERVICES</h3>
        <ul class="services-list">
          <li>PUMPING</li>
          <li>INSPECTIONS</li>
          <li>INSTALLS AND REPAIRS</li>
        </ul>
      </div>
    </section>
  </main>
</body>
</html>
```